mapleridgegroup Business Card Design

Business card with logo design for mapleridgegroup. We are a group of professional project managers based on the Pareto Principle that 80% of the work is done by 20% of the people. I have a makeshift logo that uses a pi chart with 30% and 20% and the 20% pie slice is set slightly out and up. Have played around with a teal and orange colour scheme.

Industry/Entity Type

Business

Contact Information for Business Card

Gareth Pembroke
Director
mapleridgegroup

0452 803716

```html
<!DOCTYPE html>
<html lang="en">
<head>
<meta charset="utf-8">
<title>mapleridgegroup Business Card</title>
<link href="https://fonts.googleapis.com/css2?family=Questrial&display=swap" rel="stylesheet">
<style>
  :root {
    --page-bg: #e6e6e7;
    --card-white: #ffffff;
    --brand-orange: #f0935e;
    --brand-teal: #2a929e;
    --text-light: #ffffff;
    --text-dark: #3f4a4e;
    --card-shadow: 0 2px 8px rgba(0, 0, 0, 0.18);
  }
  html, body {
    margin: 0;
    padding: 0;
    width: 1200px;
    height: 1000px;
    overflow: hidden;
    background: var(--page-bg);
    font-family: "Questrial", "Century Gothic", sans-serif;
  }
  .canvas {
    position: relative;
    width: 1200px;
    height: 1000px;
  }
  .card {
    position: absolute;
    left: 280px;
    width: 640px;
    height: 386px;
    background: var(--card-white);
    box-shadow: var(--card-shadow);
    overflow: hidden;
  }
  .card--front { top: 90px; }
  .card--back { top: 524px; }

  /* Front */
  .front-header {
    position: absolute;
    top: 0;
    left: 0;
    width: 100%;
    height: 121px;
    display: flex;
    align-items: center;
    justify-content: center;
  }
  .front-body {
    position: absolute;
    top: 121px;
    left: 0;
    width: 100%;
    height: 265px;
    background: var(--brand-orange);
  }
  .front-pointer {
    position: absolute;
    top: -1px;
    left: 50%;
    width: 32px;
    height: 16px;
    transform: translateX(-50%);
  }
  .contact-list {
    list-style: none;
    margin: 0;
    padding: 0;
    position: absolute;
    top: 52px;
    width: 100%;
    text-align: center;
    color: var(--text-light);
    font-size: 20px;
    line-height: 41px;
    letter-spacing: 0.2px;
  }

  /* Back */
  .back-band {
    position: absolute;
    left: 0;
    width: 100%;
    height: 40px;
    background: var(--brand-teal);
  }
  .back-band--top { top: 0; }
  .back-band--bottom { bottom: 0; }
  .back-center {
    position: absolute;
    top: 40px;
    bottom: 40px;
    left: 0;
    width: 100%;
    display: flex;
    align-items: center;
    justify-content: center;
  }

  /* Brand name */
  .brand {
    display: flex;
    align-items: center;
    gap: 10px;
    color: var(--brand-teal);
    font-weight: 400;
  }
  .brand-dot {
    border-radius: 50%;
    background: var(--brand-orange);
    flex: none;
  }
  .brand--small { font-size: 19px; }
  .brand--small .brand-dot { width: 18px; height: 18px; }
  .brand--large { font-size: 30px; gap: 14px; }
  .brand--large .brand-dot { width: 28px; height: 28px; }
</style>
</head>
<body>
<main class="canvas">

  <section class="card card--front" aria-label="Business card front">
    <header class="front-header">
      <div class="brand brand--small">
        <span class="brand-dot"></span>
        <span class="brand-name">mapleridge management</span>
      </div>
    </header>
    <div class="front-body">
      <svg class="front-pointer" viewBox="0 0 32 16" aria-hidden="true">
        <polygon points="0,0 32,0 16,16" fill="#ffffff"/>
      </svg>
      <ul class="contact-list">
        <li class="contact-name">Gareth Pembroke</li>
        <li class="contact-title">Director</li>
        <li class="contact-company">mapleridgegroup</li>
        <li class="contact-phone">0452 803716</li>
      </ul>
    </div>
  </section>

  <section class="card card--back" aria-label="Business card back">
    <div class="back-band back-band--top"></div>
    <div class="back-center">
      <div class="brand brand--large">
        <span class="brand-dot"></span>
        <span class="brand-name">mapleridge management</span>
      </div>
    </div>
    <div class="back-band back-band--bottom"></div>
  </section>

</main>
</body>
</html>
```